New one page Homepage with registration and log in form

Hi designers!

We need a new homepage and made a skitch of how it should be.

Can you give some of your design ideas and work it out so that it actually looks great?

Its just one page, for convertion reasons.

The logo doesnt have to be changed.

It would be cool to center the logo but not sure how design technically correct that is.

The social icons can be left out.

If you could give a few mockups than we can choose the best one.

I added one screenshot sketch of the homepage.

And 2 screenshots of what the system looks like on the inside, just so you get an idea.

Thanks

Target Market(s)

Vacation rental owners who want to increase their bookings by connecting with other VR owners and managers, or by having their own booking team for a small fee.

Industry/Entity Type

Social

Number of Pages Required

1 page

Requirements
Must have
• Use your imagination please
Nice to have
• Use your imagination
• It will be a one page design so we need to impress :)
• Keep it compact, maybe a web 3.0 flat design, etc
Should not have
• Other pages.

```html
<!DOCTYPE html>
<html lang="en">
<head>
<meta charset="utf-8">
<title>RentalNest – The First Social Booking Network</title>
<link href="https://fonts.googleapis.com/css2?family=Arimo:wght@400;700&display=swap" rel="stylesheet">
<style>
  :root {
    --orange: #ff6a00;
    --orange-panel: #ff7a1a;
    --blue: #0048a8;
    --charcoal: #363432;
    --field: #e6e5e6;
    --field-text: #8a8a8a;
    --white: #ffffff;
    --black: #000000;
    --social-blue: #334f8e;
    --circle-blue: #3b5a98;
    --circle-teal: #1a86c1;
    --circle-red: #d9302a;
  }
  * { box-sizing: border-box; margin: 0; padding: 0; }
  html, body { width: 1200px; height: 1130px; overflow: hidden; }
  body {
    position: relative;
    background: var(--white);
    font-family: "Arimo", Arial, sans-serif;
    color: var(--white);
  }
  .site-header { position: absolute; left: 0; top: 0; width: 1200px; height: 116px; }
  .brand { position: absolute; left: 106px; top: 38px; color: var(--blue); }
  .brand-name { font-size: 40px; font-weight: 700; line-height: 48px; }
  .social-links { position: absolute; left: 927px; top: 40px; display: flex; gap: 19px; }
  .social-dot { width: 45px; height: 45px; border-radius: 50%; }
  .social-dot.one { background: var(--circle-blue); }
  .social-dot.two { background: var(--circle-teal); }
  .social-dot.three { background: var(--circle-red); }
  .header-rule { position: absolute; left: 0; top: 116px; width: 1200px; height: 4px; background: var(--orange); }

  .crowd-photo {
    position: absolute; top: 120px; height: 355px;
    background: linear-gradient(180deg, #9a9a9a 0%, #bdbdbd 55%, #e8e8e8 100%);
  }
  .crowd-photo.left { left: 0; width: 589px; }
  .crowd-photo.right { left: 1100px; width: 100px; }

  .video-player { position: absolute; left: 156px; top: 259px; width: 319px; height: 266px; }
  .video-screen { width: 319px; height: 248px; background: var(--black); position: relative; }
  .play-button {
    position: absolute; left: 133px; top: 106px; width: 53px; height: 36px;
    background: linear-gradient(#d8d8d8, #8e8e8e); border-radius: 5px;
  }
  .play-button svg { position: absolute; left: 19px; top: 9px; }
  .video-controls {
    width: 319px; height: 18px; background: linear-gradient(#f4f4f4, #cfcfcf);
    border: 1px solid #aaa; display: flex; align-items: center; gap: 8px; padding: 0 6px;
    font-size: 8px; color: #333;
  }
  .video-track { flex: 1; height: 4px; background: #999; border-radius: 2px; }

  .intro-panel {
    position: absolute; left: 589px; top: 120px; width: 511px; height: 423px;
    background: var(--orange-panel); text-align: center; padding: 20px 8px 0;
  }
  .intro-title { font-size: 39px; font-weight: 400; line-height: 47px; letter-spacing: 0.3px; }
  .intro-panel p { font-size: 14px; line-height: 19px; margin-top: 19px; }
  .intro-panel p:first-of-type { margin-top: 13px; }

  .login-panel {
    position: absolute; left: 100px; top: 543px; width: 440px; height: 464px;
    background: var(--charcoal); padding: 29px 26px 0;
    box-shadow: 0 12px 14px -8px rgba(0,0,0,0.25);
  }
  .register-panel {
    position: absolute; left: 589px; top: 543px; width: 511px; height: 462px;
    background: var(--blue); padding: 28px 44px 0;
  }
  .panel-title { font-size: 23px; font-weight: 400; line-height: 28px; }
  .panel-subtitle { font-size: 12px; letter-spacing: 0.4px; margin-top: 2px; }

  .field {
    display: block; height: 32px; background: var(--field); color: var(--field-text);
    font-size: 14px; line-height: 32px; padding-left: 19px; border: 1px solid #d0d0d0;
  }
  .field.light { background: var(--white); }
  .login-panel .field { width: 379px; }
  .login-panel .field.user { margin-top: 49px; }
  .login-panel .field.pass { margin-top: 14px; }
  .remember { display: flex; align-items: center; margin-top: 15px; font-size: 13px; }
  .checkbox { width: 17px; height: 17px; background: #cfcfcf; border-radius: 3px; margin-right: 12px; }
  .button {
    display: block; text-align: center; font-size: 14px; font-weight: 700; color: var(--white);
  }
  .button.login { width: 379px; height: 35px; line-height: 33px; background: var(--blue); border: 1px solid #2a66c0; margin-top: 35px; }
  .social-hint { width: 379px; text-align: center; font-size: 13px; letter-spacing: 0.2px; margin-top: 24px; padding-right: 14px; }
  .button.social {
    width: 235px; height: 40px; margin: 35px 0 0 65px; border-radius: 4px;
    background: linear-gradient(#4661a4, var(--social-blue)); border: 1px solid #243a70;
    display: flex; align-items: center; font-size: 17px; padding-left: 12px; gap: 18px;
  }
  .social-square { width: 26px; height: 26px; background: var(--white); border-radius: 3px; }
  .forgot { width: 379px; text-align: center; font-size: 12px; letter-spacing: 0.4px; margin-top: 31px; padding-right: 18px; }

  .register-form { margin-top: 34px; }
  .name-row { display: flex; gap: 21px; }
  .name-row .field { width: 179px; }
  .register-form .field.wide { width: 379px; margin-top: 14px; }
  .register-form .field.wide.gap-15 { margin-top: 15px; }
  .register-form .field.wide.gap-17 { margin-top: 17px; }
  .button.submit { width: 379px; height: 35px; line-height: 35px; background: var(--orange); border: 1px solid #ff9a4d; margin-top: 20px; }

  .decor-circles {
    position: absolute; top: 860px; height: 191px;
    background: radial-gradient(circle, #e2e2e2 0%, rgba(255,255,255,0) 70%);
  }
  .decor-circles.left { left: 0; width: 100px; }
  .decor-circles.right { left: 1100px; width: 100px; }

  .site-footer {
    position: absolute; left: 0; top: 1051px; width: 1200px; height: 79px; background: var(--black);
    color: #8a8a8a; font-size: 12px; letter-spacing: 0.5px; text-align: center; line-height: 79px;
    padding-right: 22px;
  }
</style>
</head>
<body>
  <header class="site-header">
    <div class="brand">
      <div class="brand-name">RentalNest</div>
    </div>
    <nav class="social-links" aria-label="Social links">
      <span class="social-dot one"></span>
      <span class="social-dot two"></span>
      <span class="social-dot three"></span>
    </nav>
  </header>
  <div class="header-rule"></div>

  <div class="crowd-photo left" role="img" aria-label="Black and white photo of a group of smiling people standing together"></div>
  <div class="crowd-photo right" role="img" aria-label="Black and white photo of more people standing in the group"></div>

  <div class="video-player" aria-label="Intro video">
    <div class="video-screen">
      <div class="play-button">
        <svg width="16" height="18" viewBox="0 0 16 18"><path d="M0 0 L16 9 L0 18 Z" fill="#444"/></svg>
      </div>
    </div>
    <div class="video-controls">
      <svg width="8" height="9" viewBox="0 0 8 9"><path d="M0 0 L8 4.5 L0 9 Z" fill="#222"/></svg>
      <span class="video-track"></span>
      <span>0:00 / 0:00</span>
    </div>
  </div>

  <section class="intro-panel">
    <h1 class="intro-title">The First<br>Social Booking Network</h1>
    <p>RentalNest is a new Social Booking Network.<br>Vacation rental hosts and property managers can find each other,connect and chat amongst themselves for sharing reservation inquiries,services or anything you can imagine,in a convenient social environment.</p>
    <p>The Social Booking Network is absolutlely FREE. However if you want to save time and get really professional about incresing your bookings.Than you should consider having your own Booking Team.</p>
    <p>For just 2.5% your very own RentalNesters take care of all tedious online reservation management tasks for you in the most advanced,personalized and professional way possible.</p>
  </section>

  <div class="decor-circles left" role="img" aria-label="Soft grey decorative circles"></div>
  <div class="decor-circles right" role="img" aria-label="Soft grey decorative circles"></div>

  <section class="login-panel">
    <h2 class="panel-title">Login to your account</h2>
    <span class="field user">Your username or email address</span>
    <span class="field pass">Your password</span>
    <div class="remember"><span class="checkbox"></span>Would you like us to remember you?</div>
    <span class="button login">Log me in</span>
    <div class="social-hint">Sign in with your social identity</div>
    <span class="button social"><span class="social-square"></span>Login with Linkup</span>
    <div class="forgot">I forgot my username / Password</div>
  </section>

  <section class="register-panel">
    <h2 class="panel-title">Don't have an account?</h2>
    <div class="panel-subtitle">Register now to join the Free Booking Network !</div>
    <div class="register-form">
      <div class="name-row">
        <span class="field light">First Name</span>
        <span class="field">Last Name</span>
      </div>
      <span class="field wide">Username</span>
      <span class="field wide gap-15">Password</span>
      <span class="field wide gap-17">user@email.com</span>
      <span class="field wide gap-15">Set your contact number . Example:+12345678910</span>
      <span class="field wide gap-15">What's your reason for joing?</span>
      <span class="button submit">Submit</span>
    </div>
  </section>

  <footer class="site-footer">copyright 2014</footer>
</body>
</html>
```